Ironbark & Vale Construction and Developments business cards

A business card with watermark background (construction work)

Home improvement projects
House renovations
Bathroom and kitchen renovations
House extensions
New builds and granny flats

Director Tomas Verhoeven
(Phone number)
tomas@ivkbuilds.com.au
(Instagram logo) ivk_builds

```html
<!DOCTYPE html>
<html lang="en">
<head>
<meta charset="utf-8">
<title>Ironbark &amp; Vale Construction and Developments – Business Cards</title>
<link rel="stylesheet" href="https://fonts.googleapis.com/css2?family=Montserrat:wght@600;700&family=Arimo:wght@400&display=swap">
<style>
  :root {
    --bg: #1e1e1e;
    --card-dark: #444444;
    --card-light: #ffffff;
    --blue: #2f73b6;
    --ink: #2d2d2d;
    --muted: #5a5a5a;
    --white: #ffffff;
  }
  * { box-sizing: border-box; margin: 0; padding: 0; }
  html, body {
    width: 1200px; height: 1015px; overflow: hidden;
    background: var(--bg);
  }
  .stage {
    position: relative; width: 1200px; height: 1015px;
  }
  .card {
    position: absolute; left: 230px; width: 740px; height: 423px;
    overflow: hidden;
  }
  .card--back { top: 60px; background: var(--card-dark); }
  .card--front { top: 533px; background: var(--card-light); }

  /* brand block */
  .brand { text-align: center; }
  .brand__name {
    font-family: "Montserrat", sans-serif; font-weight: 700;
    color: var(--blue); line-height: 1.15;
  }
  .brand__mark {
    display: inline-block; width: 14px; height: 14px;
    background: var(--blue); margin-bottom: 10px;
  }
  .brand__tagline {
    display: inline-block; margin-top: 8px;
    font-family: Georgia, "Times New Roman", serif;
    color: var(--blue); font-size: 17px;
    border-bottom: 1.5px solid var(--blue); padding-bottom: 2px;
  }

  /* back face */
  .card--back .brand {
    position: absolute; left: 0; right: 0; top: 58px;
  }
  .card--back .brand__name { font-size: 30px; }
  .card--back .brand__name small { display: block; font-size: 19px; font-weight: 700; }
  .services {
    position: absolute; left: 0; right: 0; top: 245px; height: 130px;
    background: var(--blue);
    display: flex; flex-direction: column; justify-content: center; align-items: center;
    font-family: "Arimo", Arial, sans-serif; color: var(--white);
    font-size: 19px; line-height: 1.45; text-align: center;
  }

  /* front face */
  .card--front .brand {
    position: absolute; left: 30px; width: 330px; top: 115px;
  }
  .card--front .brand__name { font-size: 30px; }
  .card--front .brand__name small { display: block; font-size: 19px; }
  .divider {
    position: absolute; left: 370px; top: 40px; width: 1px; height: 230px;
    background: linear-gradient(to bottom, transparent, #b8b8b8 30%, #b8b8b8 70%, transparent);
  }
  .contact {
    position: absolute; left: 405px; top: 78px;
    font-family: "Arimo", Arial, sans-serif; color: var(--ink);
  }
  .contact__name {
    font-family: "Montserrat", sans-serif; font-weight: 700;
    color: var(--blue); font-size: 27px;
  }
  .contact__role { font-size: 18px; color: var(--muted); margin-bottom: 14px; }
  .contact__list { list-style: none; font-size: 17px; }
  .contact__list li {
    display: flex; align-items: center; gap: 10px; margin-bottom: 7px;
  }
  .contact__list li.social { margin-top: 14px; }
  .contact__list svg { width: 18px; height: 18px; flex: none; }
  .accent { color: var(--blue); }
  .social__dot {
    width: 18px; height: 18px; border-radius: 50%; background: var(--blue); flex: none;
  }
  .footer-shape { position: absolute; left: 0; bottom: 0; width: 740px; height: 110px; }
</style>
</head>
<body>
<main class="stage">

  <section class="card card--back" aria-label="Business card back">
    <div class="brand">
      <span class="brand__mark"></span>
      <p class="brand__name">Ironbark &amp; Vale<small>Construction and Developments</small></p>
      <p class="brand__tagline">Built to last, always!</p>
    </div>
    <div class="services">
      <p>Home improvement projects&nbsp; | &nbsp;House renovations</p>
      <p>Bathroom and kitchen renovations</p>
      <p>House extensions&nbsp; | &nbsp;New builds and granny flats</p>
    </div>
  </section>

  <section class="card card--front" aria-label="Business card front">
    <div class="brand">
      <span class="brand__mark"></span>
      <p class="brand__name">Ironbark &amp; Vale<small>Construction and Developments</small></p>
      <p class="brand__tagline">Built to last, always!</p>
    </div>

    <div class="divider"></div>

    <div class="contact">
      <p class="contact__name">Tomas Verhoeven</p>
      <p class="contact__role">Director</p>
      <ul class="contact__list">
        <li>
          <svg viewBox="0 0 24 24" aria-hidden="true"><path fill="#2f73b6" d="M6.6 10.8a15.1 15.1 0 0 0 6.6 6.6l2.2-2.2c.3-.3.7-.4 1-.2 1.1.4 2.3.6 3.6.6.6 0 1 .4 1 1V20c0 .6-.4 1-1 1A17 17 0 0 1 3 4c0-.6.4-1 1-1h3.5c.6 0 1 .4 1 1 0 1.3.2 2.5.6 3.6.1.3 0 .7-.2 1z"/></svg>
          044-908 217 365
        </li>
        <li>
          <svg viewBox="0 0 24 24" aria-hidden="true"><rect x="2" y="5" width="20" height="14" rx="1.5" fill="#2f73b6"/><path d="M3 6l9 7 9-7" fill="none" stroke="#fff" stroke-width="1.6"/></svg>
          tomas@ivkbuilds.com.au
        </li>
        <li>
          <svg viewBox="0 0 24 24" aria-hidden="true"><g fill="none" stroke="#2f73b6" stroke-width="1.8"><circle cx="12" cy="12" r="9"/><ellipse cx="12" cy="12" rx="4" ry="9"/><path d="M3 12h18M5 7h14M5 17h14"/></g></svg>
          www.<span class="accent">ivkbuilds</span>.com.au
        </li>
        <li class="social">
          <span class="social__dot"></span>
          ivk_builds
        </li>
      </ul>
    </div>

    <svg class="footer-shape" viewBox="0 0 740 110" preserveAspectRatio="none" aria-hidden="true">
      <polygon points="0,92 430,68 430,110 0,110" fill="#2f73b6"/>
      <polygon points="440,50 740,0 740,110 440,110" fill="#444444"/>
    </svg>
  </section>

</main>
</body>
</html>
```